Quimby's Yard & Garden Center Business Card Update

I need an updated Business card design for my Lawn and Garden Center. We do Landscaping installs, Lawn Mowing, Snow Removal and also have a Garden Center Retail Division. I uploaded a few of our previous business cards to give an idea of what we are starting with. The main goal of this update is to simplify and modernize the business card, not all of the services that are on the previous cards has to be on the new one but I would still like to highlight our main services. There is also a sample of our logo that Can be used in the design.

Industry/Entity Type

Landscaping

Contact Information for Business Card

Morris Quimby
Morris@Quimbysyardandgarden.example
Business (555) 201-7784
Cell (555) 318-6092

Colors

Designer to choose colors to be used in the design.

Requirements
Must have
• Services Provided :
• Landscaping
• Lawn Maintenance
• Snow Removal
• Garden Center

```html
<!DOCTYPE html>
<html lang="en">
<head>
<meta charset="utf-8">
<title>Quimby's Yard &amp; Garden Center – Business Card</title>
<link rel="stylesheet" href="https://fonts.googleapis.com/css2?family=Montserrat:wght@400;500;600;700&display=swap">
<style>
  :root {
    --backdrop: #2a2a2a;
    --card-green: #2f5e2c;
    --card-white: #f7f7f5;
    --frame-light: #e9efe6;
    --frame-grey: #d6d6d2;
    --text-light: #f2f4ef;
  }
  * { box-sizing: border-box; margin: 0; padding: 0; }
  html, body {
    width: 908px; height: 1200px; overflow: hidden;
    background: var(--backdrop);
    font-family: "Montserrat", sans-serif;
  }
  .canvas {
    position: relative; width: 908px; height: 1200px;
    display: flex; flex-direction: column; align-items: center; justify-content: center;
    gap: 90px;
  }
  .card {
    position: relative; width: 700px; height: 400px;
    box-shadow: 0 10px 30px rgba(0,0,0,.45);
  }
  .card-front { background: var(--card-green); color: var(--text-light); }
  .card-frame {
    position: absolute; inset: 20px;
    border: 2px solid var(--frame-light);
  }
  .card-back .card-frame { border: 1.5px solid var(--frame-grey); inset: 16px; }

  .email {
    position: absolute; top: 48px; left: 70px;
    font-size: 15px; letter-spacing: 1.6px; font-weight: 400;
  }
  .name { position: absolute; top: 78px; left: 66px; line-height: 1; }
  .name-first { display: block; font-size: 84px; font-weight: 700; letter-spacing: -1px; }
  .name-last {
    display: block; text-align: right; font-size: 30px; font-weight: 400;
    margin-top: 2px; padding-right: 4px;
  }
  .services {
    position: absolute; top: 196px; left: 420px;
    list-style: none; font-size: 17px; letter-spacing: 1.6px; line-height: 1.3;
  }
  .phones {
    position: absolute; left: 70px; bottom: 62px;
    font-size: 17px; letter-spacing: 1.6px; line-height: 1.3;
  }

  .card-back { background: var(--card-white); }
  .brand {
    position: absolute; inset: 0;
    display: flex; align-items: center; justify-content: center; gap: 20px;
  }
  .brand-dot { width: 70px; height: 70px; border-radius: 50%; background: var(--card-green); }
  .brand-name { font-size: 60px; font-weight: 700; color: var(--card-green); }
</style>
</head>
<body>
<main class="canvas">
  <section class="card card-front" aria-label="Business card front">
    <div class="card-frame"></div>
    <p class="email">Morris@Quimbysyardandgarden.example</p>
    <h1 class="name">
      <span class="name-first">morris</span>
      <span class="name-last">quimby</span>
    </h1>
    <ul class="services">
      <li>Services Provided:</li>
      <li>Landscaping</li>
      <li>Lawn Maintenance</li>
      <li>Snow Removal</li>
      <li>Garden Center</li>
    </ul>
    <p class="phones">Business (555) 201-7784<br>Cell (555) 318-6092</p>
  </section>

  <section class="card card-back" aria-label="Business card back">
    <div class="card-frame"></div>
    <div class="brand">
      <span class="brand-dot"></span>
      <span class="brand-name">Quimby's</span>
    </div>
  </section>
</main>
</body>
</html>
```